Garage Door Sales and Repair Website

Looking for a website theme and home page design for a garage door sales and repair company (Cedar Ridge Overhead).   We have a new logo and color scheme (attached) and need to update our website to match.  Here is the current site http://www.cedarridgeoverhead.example/
The design should lend it self to being responsive and full screen.
I like this site (http://www.brightpane-studio.example/) how it has different color blocks and I would like to have a slide show on my home page as well.  4 slides utilizing some of the following concepts Garage Opener, Garage Doors, Springs, Garage Door Repair, Specials, Free Estimate, etc...
Would like color design to match logo / business cards attached.
Call for Free Estimate with phone number should be visible on top of the page as well.

Consumers
Professional Service
1 page
Other font styles liked:
- Oswald, Open Sans, other similar google web fonts

Requirements
Must have
- 4 slides for home page design
- Free Estimate
- Phone Number

Nice to have
- Call out for online specials

```html
<!DOCTYPE html>
<html lang="en">
<head>
<meta charset="utf-8">
<title>Cedar Ridge Overhead – Garage Door Sales &amp; Repair</title>
<link rel="stylesheet" href="https://fonts.googleapis.com/css2?family=Montserrat:wght@400;500;600;700&family=Open+Sans:wght@400;600;700&display=swap">
<style>
:root{
  --slate:#4f5878;
  --slate-dark:#3f4763;
  --slate-deep:#353c55;
  --slate-field:#5e6889;
  --nav:#cfd3dc;
  --paper:#ffffff;
  --mist:#efefef;
  --ink:#2f3448;
  --muted:#6b7184;
  --line:#c8ccd6;
}
*{box-sizing:border-box;margin:0;padding:0}
html,body{width:1200px;height:3377px;overflow:hidden}
body{font-family:"Open Sans",Arial,sans-serif;color:var(--ink);background:var(--paper);position:relative}
section,header,footer{position:relative;width:1200px}
h2.section-title{position:absolute;font-family:"Montserrat",Arial,sans-serif;font-weight:500;font-size:28px;color:var(--slate);border-left:3px solid var(--slate);padding-left:10px;line-height:1.15;text-transform:uppercase;white-space:nowrap}
.btn-outline{position:absolute;border:2px solid var(--slate);border-radius:22px;font-family:"Montserrat",Arial,sans-serif;font-weight:600;font-size:13px;color:var(--slate);display:flex;align-items:center;justify-content:center;gap:10px;letter-spacing:.5px}

/* hero + header */
.hero{height:596px;background:linear-gradient(180deg,#b9ad99 0%,#a99d88 45%,#978b76 100%);overflow:hidden}
.hero-photo{position:absolute;left:0;top:190px;width:1200px;height:406px;background:linear-gradient(90deg,#a69a84 0%,#c4bba9 35%,#d9d6cd 50%,#c6bdac 68%,#a29681 100%)}
.hero-door{position:absolute;left:575px;top:236px;width:535px;height:330px;background:linear-gradient(180deg,#eeeeea,#d9d9d4);border:10px solid #f4f4f1}
.topbar{position:absolute;left:0;top:0;width:1200px;height:140px;background:var(--slate)}
.logo{position:absolute;left:75px;top:22px;display:flex;align-items:center;gap:10px}
.logo-mark{width:26px;height:26px;border-radius:50%;background:#fff}
.logo-name{font-family:"Montserrat",Arial,sans-serif;font-weight:700;font-size:22px;color:#fff;line-height:1.1;width:150px}
.contact-chip{position:absolute;top:40px;display:flex;align-items:center;gap:14px;color:#fff}
.chip-icon{width:56px;height:56px;border-radius:50%;border:2px solid rgba(255,255,255,.6);display:flex;align-items:center;justify-content:center}
.chip-text{font-size:13px;line-height:1.35}
.chip-phone{font-family:"Montserrat",Arial,sans-serif;font-size:28px;font-weight:500;line-height:1}
.nav{position:absolute;left:270px;top:140px;width:930px;height:51px;background:var(--nav);display:flex;align-items:center;padding-left:22px}
.nav a{font-family:"Montserrat",Arial,sans-serif;font-size:12.5px;font-weight:500;color:var(--slate-dark);text-decoration:none;padding:0 12px;border-right:1px solid #aab0be;line-height:14px}
.nav a:last-of-type{border-right:0}
.nav .nav-cta{position:absolute;right:75px;top:0;height:51px;width:175px;background:var(--slate);color:#fff;font-weight:600;font-size:13px;display:flex;align-items:center;justify-content:center}
.hero-title{position:absolute;left:75px;top:282px;font-family:"Montserrat",Arial,sans-serif;font-weight:700;font-size:34px;line-height:41px;color:#fff;text-transform:uppercase;width:480px}
.hero-rule{position:absolute;left:75px;top:436px;width:70px;height:3px;background:#fff}
.hero .btn-outline{left:75px;top:474px;width:190px;height:40px;border-color:#fff;color:#fff}
.dots{position:absolute;display:flex;gap:6px}
.dots span{width:10px;height:10px;border-radius:50%;background:#bfc3cd}
.dots span.on{background:var(--slate)}

/* about */
.about{height:434px}
.about-copy{position:absolute;left:75px;width:700px;font-size:12.5px;line-height:1.5;color:var(--ink)}
.features{position:absolute;left:75px;width:700px;display:grid;grid-template-columns:1fr 1fr;column-gap:22px;row-gap:14px}
.feature{border-left:1px solid var(--line);padding-left:12px}
.feature h3{font-family:"Montserrat",Arial,sans-serif;font-size:12.5px;font-weight:600;color:var(--slate);text-transform:uppercase}
.feature p{font-size:11.5px;line-height:1.4;color:var(--ink)}
.about .btn-outline{left:75px;width:350px;height:40px}
.video{position:absolute;left:790px;width:335px;height:292px;background:linear-gradient(160deg,#9aa2ad,#c9ccd0 50%,#7f8791)}
.play{position:absolute;left:130px;top:108px;width:76px;height:76px;border-radius:50%;background:#fff;display:flex;align-items:center;justify-content:center}

/* specials */
.specials{height:500px;background:var(--slate)}
.specials h2{position:absolute;font-family:"Montserrat",Arial,sans-serif;font-weight:500;font-size:27px;color:#fff;text-transform:uppercase;white-space:nowrap}
.checklist{position:absolute;left:75px;width:450px;list-style:none}
.checklist li{display:flex;align-items:center;gap:16px;height:30px;margin-bottom:1px;background:var(--slate-field);padding-left:10px;font-size:19px;color:#f1f2f6}
.tick{width:14px;height:14px;background:#e6e8ee;display:flex;align-items:center;justify-content:center}
.offer{position:absolute;width:172px;height:172px;border-radius:50%;background:rgba(255,255,255,.07);border:2px solid rgba(255,255,255,.12);display:flex;flex-direction:column;align-items:center;justify-content:center;color:#fff;text-align:center}
.offer b{font-family:"Montserrat",Arial,sans-serif;font-weight:700;font-size:30px;line-height:1;white-space:nowrap;letter-spacing:-.5px}
.offer i{font-style:normal;font-family:"Montserrat",Arial,sans-serif;font-weight:700;font-size:12px;border-top:1px solid #fff;margin-top:3px;padding-top:1px;white-space:nowrap}
.offer small{font-size:7px;opacity:.8;margin-top:2px;white-space:nowrap}
.estimate-form{position:absolute;left:774px;width:351px}
.field{height:42px;border-radius:12px;background:var(--slate-field);margin-bottom:7px;color:#aeb4c6;font-size:13px;display:flex;align-items:center;padding-left:20px;justify-content:space-between;padding-right:20px}
.field.select{color:#fff}
.field.area{height:130px;align-items:flex-start;padding-top:14px}
.submit{height:42px;border-radius:21px;background:#fff;color:var(--slate);font-family:"Montserrat",Arial,sans-serif;font-weight:600;font-size:14px;display:flex;align-items:center;justify-content:center;gap:8px;margin-top:10px}

/* services */
.services{height:389px}
.services h2.section-title{font-size:25px;line-height:1.25}
.services-copy{position:absolute;left:75px;width:270px;font-size:14px;line-height:1.55;color:var(--ink);text-align:justify}
.services .btn-outline{left:75px;width:258px;height:40px}
.svc{position:absolute;width:367px;height:133px;background:linear-gradient(135deg,#2e2f35,#4a4b52 60%,#5a5b60);padding:22px 20px 0 100px;color:#fff}
.svc-icon{position:absolute;left:22px;top:38px;width:58px;height:58px;border-radius:50%;background:var(--slate);display:flex;align-items:center;justify-content:center}
.svc h3{font-family:"Montserrat",Arial,sans-serif;font-size:12.5px;font-weight:600;text-transform:uppercase;margin-bottom:4px}
.svc p{font-size:11.5px;line-height:1.4;color:#d9dae0}

/* blog */
.blog{height:471px;background:var(--mist)}
.post{position:absolute;width:331px;height:286px;overflow:hidden}
.post-photo{position:absolute;inset:0}
.post-meta{position:absolute;left:24px;bottom:55px;display:flex;align-items:center;gap:8px;color:#fff;font-size:11px;font-weight:700}
.post-meta .clock{width:16px;height:16px;border-radius:50%;border:2px solid #fff}
.post-rule{position:absolute;left:0;right:0;bottom:48px;height:1px;background:rgba(255,255,255,.4)}
.post h3{position:absolute;left:24px;bottom:18px;color:#fff;font-family:"Montserrat",Arial,sans-serif;font-weight:600;font-size:13.5px;text-transform:uppercase}

/* testimonials */
.testimonials{height:360px}
.quote-box{position:absolute;left:75px;width:1050px;height:122px;border:2px solid var(--slate);padding:36px 40px 0 96px;font-size:15px;line-height:1.5;color:var(--ink)}
.quote-mark{position:absolute;left:30px;top:20px;font-family:Georgia,serif;font-size:72px;line-height:1;color:var(--slate);font-weight:700}
.quote-tail{position:absolute;left:70px}
.author{position:absolute;left:75px;display:flex;align-items:center;gap:14px}
.avatar{width:50px;height:50px;border-radius:50%;background:linear-gradient(135deg,#c7cbd3,#8b93a4)}
.author b{display:block;font-family:"Montserrat",Arial,sans-serif;font-size:17px;color:var(--ink);font-weight:600}
.author span{font-size:13px;color:var(--muted)}

/* newsletter */
.newsletter{height:168px;background:var(--mist)}
.newsletter p{position:absolute;left:75px;width:440px;font-size:12.5px;line-height:1.45}
.news-input{position:absolute;left:529px;width:596px;height:40px;border-radius:20px;border:1px solid #bcc1cb;background:#fff;font-size:12.5px;color:#9aa0ad;display:flex;align-items:center;padding-left:26px}
.news-btn{position:absolute;right:0;top:-1px;width:150px;height:40px;border-radius:20px;background:var(--slate);color:#fff;font-family:"Montserrat",Arial,sans-serif;font-weight:600;font-size:13px;display:flex;align-items:center;justify-content:center;gap:8px}

/* footer */
.site-footer{height:356px;background:var(--slate)}
.foot-logo{position:absolute;left:75px;display:flex;align-items:center;gap:10px}
.badge{position:absolute;background:rgba(255,255,255,.85)}
.foot-about{position:absolute;left:75px;width:665px;color:#eef0f5;font-size:15.5px;line-height:1.8;text-align:justify}
.foot-col{position:absolute;left:774px;color:#fff}
.foot-col h3{font-family:"Montserrat",Arial,sans-serif;font-size:17px;font-weight:600;padding-bottom:12px;border-bottom:1px solid rgba(255,255,255,.35);width:351px}
.foot-list{list-style:none;margin-top:14px}
.foot-list li{display:flex;align-items:center;gap:16px;font-size:12.5px;height:32px}
.social{display:flex;gap:8px;margin-top:14px}
.social span{width:24px;height:24px;background:#fff;border-radius:2px}
.copyright{position:absolute;left:0;top:3274px;width:1200px;height:103px;background:var(--slate-deep);color:#e4e6ee;font-size:13px;display:flex;align-items:center;justify-content:center}
</style>
</head>
<body>

<header class="hero">
  <div class="hero-photo" role="img" aria-label="House facade with tan siding, wall lanterns and a white raised-panel garage door"></div>
  <div class="hero-door" role="img" aria-label="White sectional garage door"></div>
  <div class="topbar"></div>
  <div class="logo"><span class="logo-mark"></span><span class="logo-name">Cedar Ridge Overhead</span></div>
  <div class="contact-chip" style="left:574px">
    <span class="chip-icon"><svg width="22" height="26" viewBox="0 0 22 26"><path d="M11 1a9 9 0 0 0-9 9c0 7 9 15 9 15s9-8 9-15a9 9 0 0 0-9-9z" fill="none" stroke="#fff" stroke-width="2"/><circle cx="11" cy="10" r="3" fill="#fff"/></svg></span>
    <span class="chip-text">2750 Larkspur Court<br>Westfield, CO 80099</span>
  </div>
  <div class="contact-chip" style="left:862px">
    <span class="chip-icon"><svg width="24" height="24" viewBox="0 0 24 24"><path d="M5 2l4 1 2 5-3 2c1 3 3 5 6 6l2-3 5 2 1 4c-1 2-3 3-5 3C9 21 3 15 2 7c0-2 1-4 3-5z" fill="none" stroke="#fff" stroke-width="1.8"/></svg></span>
    <span><span class="chip-phone">555-014-2290</span><br><span class="chip-text">info@cedarridgeoverhead.example</span></span>
  </div>
  <nav class="nav">
    <a>HOME</a><a>ABOUT</a><a>OUR SERVICES</a><a>TESTIMONIAL</a><a>BLOG</a><a>FAQ'S</a><a>CONTACT US</a>
    <a class="nav-cta">GET FREE ESTIMATE</a>
  </nav>
  <h1 class="hero-title">Denver's Preferred Garage Door Sales and Repair Company</h1>
  <div class="hero-rule"></div>
  <a class="btn-outline">KNOW MORE <svg width="14" height="10" viewBox="0 0 14 10"><path d="M0 5h12M8 1l4 4-4 4" fill="none" stroke="#fff" stroke-width="2"/></svg></a>
  <div class="dots" style="left:576px;top:576px"><span class="on"></span><span></span><span></span></div>
</header>

<section class="about">
  <h2 class="section-title" style="left:75px;top:70px">About Us</h2>
  <p class="about-copy" style="top:104px">Cedar Ridge Overhead Door Sales and Repair (Cedar Ridge Overhead) is a locally owned and operated garage door company that specializes in everything from garage door repairs to installation of new garage doors to garage door service and installation of garage door openers.</p>
  <div class="features" style="top:168px">
    <div class="feature"><h3>Honesty</h3><p>Our reputation is important to us and so is your satisfaction. No hidden costs or un-needed add-ons!</p></div>
    <div class="feature"><h3>24 Emergency Service</h3><p>Our Technicians are available 24 hours a day 7 days a week. No extra charge for weekends</p></div>
    <div class="feature"><h3>Dependability</h3><p>Fast, friendly reliable service from qualified technicians.</p></div>
    <div class="feature"><h3>Free Estimates</h3><p>Don't get blindsided by unexpected sur-charges etc, get a free quote today.</p></div>
    <div class="feature"><h3>Satisfaction Guaranteed</h3><p>We guarantee all our work</p></div>
  </div>
  <a class="btn-outline" style="top:347px">SCHEDULE FREE ESTIMATE <svg width="14" height="10" viewBox="0 0 14 10"><path d="M0 5h12M8 1l4 4-4 4" fill="none" stroke="#4f5878" stroke-width="2"/></svg></a>
  <div class="video" style="top:70px" role="img" aria-label="Video still of white carriage-style garage doors">
    <span class="play"><svg width="28" height="32" viewBox="0 0 28 32"><path d="M4 2l22 14L4 30z" fill="#4f5878"/></svg></span>
  </div>
</section>

<section class="specials">
  <h2 style="left:75px;top:42px">Same Day Garage Door Repair &amp; Service!</h2>
  <ul class="checklist" style="top:102px">
    <li><span class="tick"><svg width="10" height="8" viewBox="0 0 10 8"><path d="M1 4l3 3 5-6" fill="none" stroke="#4f5878" stroke-width="2"/></svg></span>Fast.</li>
    <li><span class="tick"><svg width="10" height="8" viewBox="0 0 10 8"><path d="M1 4l3 3 5-6" fill="none" stroke="#4f5878" stroke-width="2"/></svg></span>Affordable.</li>
    <li><span class="tick"><svg width="10" height="8" viewBox="0 0 10 8"><path d="M1 4l3 3 5-6" fill="none" stroke="#4f5878" stroke-width="2"/></svg></span>Professional.</li>
    <li><span class="tick"><svg width="10" height="8" viewBox="0 0 10 8"><path d="M1 4l3 3 5-6" fill="none" stroke="#4f5878" stroke-width="2"/></svg></span>No additional charge for weekends.</li>
    <li><span class="tick"><svg width="10" height="8" viewBox="0 0 10 8"><path d="M1 4l3 3 5-6" fill="none" stroke="#4f5878" stroke-width="2"/></svg></span>24 hour emergency service available.</li>
  </ul>
  <div class="offer" style="left:567px;top:97px"><b>$60 OFF</b><i>SPRING REPLACEMENT</i><small>With any replacement of springs</small></div>
  <div class="offer" style="left:72px;top:298px"><b>$100 OFF</b><i>NEW GARAGE DOOR</i><small>Purchase and installation only</small></div>
  <div class="offer" style="left:313px;top:298px"><b>$200 OFF</b><i>NEW GARAGE DOOR</i><small>Purchase and installation only</small></div>
  <div class="offer" style="left:556px;top:298px"><b>$325 OFF</b><i>BEST VALUE</i><small>Door, opener and install package</small></div>
  <h2 style="left:774px;top:42px">Get Free Estimate Now</h2>
  <form class="estimate-form" style="top:92px">
    <div class="field">Your Name (required)</div>
    <div class="field">Your Email (required)</div>
    <div class="field">Your Mobile Number (required)</div>
    <div class="field select">Select Service <svg width="10" height="6" viewBox="0 0 10 6"><path d="M0 0h10L5 6z" fill="#fff"/></svg></div>
    <div class="field area">Your Message</div>
    <div class="submit">REQUEST NOW <svg width="14" height="10" viewBox="0 0 14 10"><path d="M0 5h12M8 1l4 4-4 4" fill="none" stroke="#4f5878" stroke-width="2"/></svg></div>
  </form>
</section>

<section class="services">
  <h2 class="section-title" style="left:80px;top:48px">Our Best<br>Services For You</h2>
  <p class="services-copy" style="top:141px">Lorem Ipsum is simply dummy text of the printing and typesetting industry. Lorem Ipsum has been the industry's standard dummy text ever since the 1500s, when an unknown printer took a galley of type and scrambled.</p>
  <a class="btn-outline" style="top:304px">SCHEDULE FREE ESTIMATE <svg width="14" height="10" viewBox="0 0 14 10"><path d="M0 5h12M8 1l4 4-4 4" fill="none" stroke="#4f5878" stroke-width="2"/></svg></a>
  <div class="svc" style="left:367px;top:52px" role="img" aria-label="Garage door repair service, dark photo background">
    <span class="svc-icon"><svg width="28" height="24" viewBox="0 0 28 24"><path d="M2 9L14 2l12 7v13H2z M7 12h14v10H7z M7 15h14M7 18h14" fill="none" stroke="#fff" stroke-width="1.8"/></svg></span>
    <h3>Garage Door Repair</h3><p>Cedar Ridge Overhead offers complete garage door repair and door maintenance services. Damaged panels, bent tracks...</p>
  </div>
  <div class="svc" style="left:758px;top:52px" role="img" aria-label="Garage door openers service, dark photo background">
    <span class="svc-icon"><svg width="28" height="22" viewBox="0 0 28 22"><path d="M3 4h22v8H3z M8 12l-4 8 M20 12l4 8 M8 8h12" fill="none" stroke="#fff" stroke-width="1.8"/></svg></span>
    <h3>Garage Door Openers</h3><p>Cedar Ridge Overhead offers a complete line of Garage Door Openers and accessories, from top manufacturers like Northgate and Hollis Lift.</p>
  </div>
  <div class="svc" style="left:367px;top:209px" role="img" aria-label="New garage doors service, dark photo background">
    <span class="svc-icon"><svg width="28" height="24" viewBox="0 0 28 24"><path d="M2 9L14 2l12 7v13H2z M7 12h14v10H7z" fill="none" stroke="#fff" stroke-width="1.8"/><path d="M20 4v6" stroke="#fff" stroke-width="1.8"/></svg></span>
    <h3>New Garage Doors</h3><p>Cedar Ridge Overhead installs new garage doors. We will come to your home, take measurements, discuss your options with you...</p>
  </div>
  <div class="svc" style="left:758px;top:209px" role="img" aria-label="Broken springs service, dark photo background">
    <span class="svc-icon"><svg width="30" height="20" viewBox="0 0 30 20"><path d="M2 10c2-8 4-8 5 0s3 8 5 0 3-8 5 0 3 8 5 0 3-8 5 0" fill="none" stroke="#fff" stroke-width="1.8"/></svg></span>
    <h3>Broken Springs</h3><p>Cedar Ridge Overhead is your local garage door spring replacement expert! We replace broken torsion springs, extension springs...</p>
  </div>
</section>

<section class="blog">
  <h2 class="section-title" style="left:75px;top:68px">From Our Blog</h2>
  <article class="post" style="left:75px;top:131px">
    <div class="post-photo" role="img" aria-label="Carriage-style garage doors on a gray sided house" style="background:linear-gradient(180deg,#6f7a84,#4f5660 55%,#2c3036)"></div>
    <div class="post-meta"><span class="clock"></span>JUN 8, 2016</div><div class="post-rule"></div>
    <h3>Garage Door Maintenance Tips</h3>
  </article>
  <article class="post" style="left:436px;top:131px">
    <div class="post-photo" role="img" aria-label="Interior view of a garage door opener and rails" style="background:linear-gradient(180deg,#7d7c72,#4f4e47 55%,#2b2a27)"></div>
    <div class="post-meta"><span class="clock"></span>JUN 8, 2016</div><div class="post-rule"></div>
    <h3>Northgate's Latest Opener</h3>
  </article>
  <article class="post" style="left:794px;top:131px">
    <div class="post-photo" role="img" aria-label="Modern glass garage doors lit at dusk" style="background:linear-gradient(180deg,#4b3a2e,#6e5a46 45%,#2a241f)"></div>
    <div class="post-meta"><span class="clock"></span>JUN 8, 2016</div><div class="post-rule"></div>
    <h3>Garage Door Maintenance Tips</h3>
  </article>
</section>

<section class="testimonials">
  <h2 class="section-title" style="left:75px;top:62px">Testimonials</h2>
  <blockquote class="quote-box" style="top:114px"><span class="quote-mark">&ldquo;</span>Lorem Ipsum is simply dummy text of the printing and typesetting industry. Lorem Ipsum has been the industry's standard dummy text ever since the 1500s, when an unknown printer took a galley of type.</blockquote>
  <svg class="quote-tail" style="top:234px" width="30" height="18" viewBox="0 0 30 18"><path d="M0 0L15 16 30 0" fill="#fff" stroke="#4f5878" stroke-width="2"/></svg>
  <div class="author" style="top:258px"><span class="avatar" role="img" aria-label="Customer portrait"></span><div><b>Dana Whitfield</b><span>Director</span></div></div>
  <div class="dots" style="left:1097px;top:264px"><span class="on" style="width:6px;height:6px"></span><span style="width:6px;height:6px"></span><span style="width:6px;height:6px"></span></div>
</section>

<section class="newsletter">
  <h2 class="section-title" style="left:75px;top:40px">Our Newsletter</h2>
  <p style="top:96px">Lorem Ipsum is simply dummy text of the printing and typesetting industry. Lorem Ipsum has been the industry's standard.</p>
  <div class="news-input" style="top:68px">Enter your email address
    <span class="news-btn">SUBSCRIBE <svg width="14" height="10" viewBox="0 0 14 10"><path d="M0 5h12M8 1l4 4-4 4" fill="none" stroke="#fff" stroke-width="2"/></svg></span>
  </div>
</section>

<footer class="site-footer">
  <div class="foot-logo" style="top:62px"><span class="logo-mark"></span><span class="logo-name">Cedar Ridge Overhead</span></div>
  <div class="badge" style="left:270px;top:36px;width:158px;height:134px;border-radius:50%;opacity:.5" role="img" aria-label="Service award badge"></div>
  <div class="badge" style="left:458px;top:26px;width:94px;height:152px;border-radius:4px" role="img" aria-label="Accreditation badge"></div>
  <div class="badge" style="left:580px;top:32px;width:150px;height:150px;border-radius:50%;background:#e8b92c" role="img" aria-label="Listing award badge"></div>
  <p class="foot-about" style="top:204px">We are dedicated to the highest quality professional service and complete customer satisfaction. We take pride in serving our customers and providing the best possible service experience on each appointment we schedule, and we maintain our reputation by being honest and dependable.</p>
  <div class="foot-col" style="top:54px">
    <h3>Contact Us</h3>
    <ul class="foot-list">
      <li><svg width="12" height="15" viewBox="0 0 12 15"><path d="M6 0a6 6 0 0 0-6 6c0 4 6 9 6 9s6-5 6-9a6 6 0 0 0-6-6z" fill="#fff"/></svg>Cedar Ridge Overhead, Alder Blvd, Westfield, CO 80099</li>
      <li><svg width="13" height="13" viewBox="0 0 24 24"><path d="M5 2l4 1 2 5-3 2c1 3 3 5 6 6l2-3 5 2 1 4c-1 2-3 3-5 3C9 21 3 15 2 7c0-2 1-4 3-5z" fill="#fff"/></svg>555-014-2290</li>
      <li><svg width="14" height="11" viewBox="0 0 14 11"><rect width="14" height="11" fill="#fff"/><path d="M0 0l7 6 7-6" fill="none" stroke="#4f5878" stroke-width="1.5"/></svg>info@cedarridgeoverhead.example</li>
    </ul>
  </div>
  <div class="foot-col" style="top:254px">
    <h3 style="border:0;padding:0">Follow Us</h3>
    <div class="social"><span></span><span></span><span></span></div>
  </div>
</footer>
<div class="copyright">Copyright © 2008 - 2016 Cedar Ridge Overhead, LLC. All rights reserved.</div>

</body>
</html>
```